SipNOW Business Cards

Hi designers!

Here's some background on our start-up and this project:

SipNOW is a website that will allow users to order alcohol from nearby liquor stores and have it delivered to their homes in minutes. We are really excited to work on creating the best online, alcohol purchasing experience for the users.

So why SipNOW? We like to think of ourselves as that great friend who will get alcohol for you because he happens to have a car. We help you drink in with your friends, family, or guests. Our site will target students and young professionals (of drinking age) who are comfortable buying things online or through apps. We don't see this service as a luxury, VIP, or niche service in the least; instead, we think of us as a relaxed, service-driven start-up that believes in simple design and transparent .

Now, we want a business card that incorporates our newly acquired logo design and some complimenting colors and fonts. Feel free to do it single or double sided, although I'm a sucker for double...

If you happen to have any questions, want to throw some ideas around, or just want some feedback- email me at marco@sipnow.example.

Marco Tessin
Founder

Industry/Entity Type

Business

Requirements
Must have
• Name, Position, Email, Cell-phone

No address, no fax, no land-line.

```html
<!DOCTYPE html>
<html lang="en">
<head>
<meta charset="utf-8">
<title>SipNOW Business Cards</title>
<link rel="stylesheet" href="https://fonts.googleapis.com/css2?family=Bebas+Neue&family=Open+Sans:wght@400&display=swap">
<style>
  :root {
    --sun-yellow: #f8c51c;
    --ink-black: #050404;
    --paper-white: #ffffff;
    --card-edge: #b9b9b9;
    --label-grey: #555555;
  }
  * { margin: 0; padding: 0; box-sizing: border-box; }
  html, body {
    width: 1200px;
    height: 1000px;
    overflow: hidden;
    background: var(--paper-white);
  }
  .board {
    position: relative;
    width: 1200px;
    height: 1000px;
  }
  .card {
    position: absolute;
    overflow: hidden;
  }
  .card-front {
    left: 66px; top: 56px;
    width: 494px; height: 286px;
    background: var(--paper-white);
    border: 1px solid var(--card-edge);
    display: flex;
    align-items: center;
    justify-content: center;
  }
  .wordmark {
    display: flex;
    align-items: center;
    gap: 14px;
    margin-top: 8px;
  }
  .wordmark-name {
    font-family: "Bebas Neue", sans-serif;
    font-size: 104px;
    line-height: 1;
    letter-spacing: 1px;
    color: var(--ink-black);
  }
  .wordmark-dot {
    width: 22px; height: 22px;
    background: var(--sun-yellow);
  }
  .card-back {
    left: 613px; top: 58px;
    width: 492px; height: 281px;
    background: var(--sun-yellow);
  }
  .holder {
    position: absolute;
    top: 60px; left: 0; right: 0;
    text-align: center;
    font-family: "Bebas Neue", sans-serif;
    color: var(--ink-black);
  }
  .holder-name { font-size: 38px; line-height: 30px; letter-spacing: 0.5px; }
  .holder-role { font-size: 24px; line-height: 22px; letter-spacing: 0.5px; }
  .contact-band {
    position: absolute;
    left: 0; right: 0;
    top: 119px; height: 110px;
    background: var(--ink-black);
  }
  .contact {
    position: absolute;
    z-index: 2;
    top: 27px; left: 0; width: 492px;
    text-align: center;
    font-family: "Bebas Neue", sans-serif;
    font-size: 23px;
    line-height: 26px;
    letter-spacing: 0.4px;
    color: var(--paper-white);
  }
  .bottle-art {
    position: absolute;
    z-index: 1;
    left: 378px; top: 119px;
    width: 80px; height: 110px;
  }
  .side-label {
    position: absolute;
    top: 352px;
    width: 300px;
    text-align: center;
    font-family: "Open Sans", sans-serif;
    font-size: 34px;
    color: var(--label-grey);
  }
  .side-label-front { left: 163px; }
  .side-label-back { left: 704px; }
</style>
</head>
<body>
<main class="board">
  <section class="card card-front">
    <div class="wordmark">
      <span class="wordmark-name">SipNOW</span>
      <span class="wordmark-dot"></span>
    </div>
  </section>

  <section class="card card-back">
    <div class="holder">
      <div class="holder-name">Marco Tessin</div>
      <div class="holder-role">Founder</div>
    </div>
    <div class="contact-band"></div>
    <div class="contact" style="top:146px">
      <div class="contact-email">marco@sipnow.example</div>
      <div class="contact-phone">555-0142-87</div>
    </div>
    <svg class="bottle-art" viewBox="0 0 80 110" role="img" aria-label="Tilted bottle silhouette with a motion-blur trail">
      <defs>
        <linearGradient id="bottleGlow" x1="0" y1="0" x2="1" y2="0">
          <stop offset="0" stop-color="#050404"/>
          <stop offset="0.55" stop-color="#7a6010"/>
          <stop offset="1" stop-color="#f8c51c"/>
        </linearGradient>
      </defs>
      <rect x="0" y="0" width="80" height="110" fill="url(#bottleGlow)"/>
    </svg>
  </section>

  <div class="side-label side-label-front">Front</div>
  <div class="side-label side-label-back">Back</div>
</main>
</body>
</html>
```